Vodka label for New Brand called HOLT Vodka

We need a label measuring 3.5 inches wide & 5 inches tall for this vodka bottle. The brand is "HOLT Vodka". This should be the largest font on the label. "Handcrafted in the USA" should be on bottle in small font near the bottom. The tagline "Here's Our Liquid Toast" also needs to be included anywhere that makes sense in a smaller font than the brand name. Also in smaller font at the bottom/corners- "80 proof, 750 ml, 40% alc/vol" I value the human mind over AI, but am providing a couple designs that were AI generated to give you a better idea where to start and what we are looking for. Thank you!
Updates

Target Market(s)

21-45 year olds.

Industry/Entity Type

Alcohol

Colors
0054AA
0677BA
7BADD7
CADEEF
E8F1F8
EB3D1F
EC4F4E
F09395
F8D3D4
FCEDEE

Requirements
Should not have
• You can not use the US flag but can use elements of it.

```html
<!DOCTYPE html>
<html lang="en">
<head>
<meta charset="utf-8">
<title>HOLT Vodka – Bottle Label</title>
<link rel="stylesheet" href="https://fonts.googleapis.com/css2?family=Marcellus&family=Cinzel:wght@700&family=Crimson+Text&family=Oswald:wght@500&display=swap">
<style>
  :root {
    --navy: #1f2d6b;
    --panel-blue: #283d84;
    --panel-blue-light: #34499a;
    --flag-red: #c9352b;
    --paper: #f5f5f7;
    --bg-top: #d7e2ef;
    --bg-mid: #eef3f9;
    --bg-bottom: #b9c8de;
  }
  html, body {
    margin: 0;
    padding: 0;
    overflow: hidden;
  }
  body {
    width: 960px;
    height: 1200px;
    background: linear-gradient(180deg, var(--bg-top) 0%, var(--bg-mid) 50%, var(--bg-bottom) 100%);
    display: flex;
    align-items: center;
    justify-content: center;
  }
  .label {
    display: block;
    width: 620px;
    height: 1109px;
  }
  .brand-name {
    font-family: "Marcellus", serif;
    fill: var(--paper);
  }
  .product-type {
    font-family: "Cinzel", serif;
    font-weight: 700;
    fill: var(--paper);
  }
  .tagline {
    font-family: "Crimson Text", serif;
    fill: var(--paper);
  }
  .spec {
    font-family: "Oswald", sans-serif;
    font-weight: 500;
    fill: var(--paper);
  }
  .origin {
    font-family: "Oswald", sans-serif;
    font-weight: 500;
    fill: var(--navy);
  }
</style>
</head>
<body>
<svg class="label" viewBox="0 0 520 930" xmlns="http://www.w3.org/2000/svg" aria-label="HOLT Vodka label">
  <defs>
    <linearGradient id="panel-fill" x1="0" y1="0" x2="0" y2="1">
      <stop offset="0" stop-color="var(--panel-blue-light)"/>
      <stop offset="1" stop-color="var(--panel-blue)"/>
    </linearGradient>
  </defs>

  <rect class="label-ground" x="0" y="0" width="520" height="930" fill="var(--paper)"/>
  <rect class="top-band" x="0" y="0" width="520" height="18" fill="var(--navy)"/>

  <g class="stripes" fill="var(--flag-red)">
    <rect x="0" y="38" width="520" height="31"/>
    <rect x="0" y="100" width="520" height="31"/>
    <rect x="0" y="162" width="520" height="31"/>
    <rect x="0" y="224" width="520" height="31"/>
    <rect x="0" y="286" width="520" height="31"/>
    <rect x="0" y="348" width="520" height="31"/>
    <rect x="0" y="410" width="520" height="31"/>
    <rect x="0" y="472" width="520" height="31"/>
    <rect x="0" y="534" width="520" height="31"/>
    <rect x="0" y="596" width="520" height="31"/>
    <rect x="0" y="658" width="520" height="31"/>
    <rect x="0" y="720" width="520" height="31"/>
    <rect x="0" y="770" width="520" height="30"/>
  </g>

  <path class="shield-outer" d="M260,78 L495,125 L495,730 L260,790 L25,730 L25,125 Z" fill="var(--navy)"/>
  <path class="shield-panel" role="img" aria-label="Blue panel with a faint star texture"
        d="M260,112 L468,150 L468,660 L260,725 L52,660 L52,150 Z"
        fill="url(#panel-fill)" stroke="var(--paper)" stroke-width="7" stroke-linejoin="miter"/>

  <text class="brand-name" x="260" y="380" text-anchor="middle" font-size="150" textLength="370" lengthAdjust="spacingAndGlyphs">HOLT</text>
  <text class="product-type" x="260" y="505" text-anchor="middle" font-size="52" textLength="250" lengthAdjust="spacingAndGlyphs">VODKA</text>

  <g class="tagline-block">
    <line x1="164" y1="580" x2="192" y2="580" stroke="var(--paper)" stroke-width="1.2"/>
    <line x1="164" y1="584" x2="192" y2="584" stroke="var(--paper)" stroke-width="1.2"/>
    <line x1="328" y1="580" x2="356" y2="580" stroke="var(--paper)" stroke-width="1.2"/>
    <line x1="328" y1="584" x2="356" y2="584" stroke="var(--paper)" stroke-width="1.2"/>
    <text class="tagline" x="260" y="588" text-anchor="middle" font-size="18" letter-spacing="0.5">HERE'S OUR</text>
    <text class="tagline" x="260" y="619" text-anchor="middle" font-size="29" letter-spacing="0.5">LIQUID</text>
    <text class="tagline" x="260" y="645" text-anchor="middle" font-size="18" letter-spacing="0.8">TOAST</text>
  </g>

  <rect class="spec-band" x="0" y="800" width="520" height="55" fill="var(--navy)"/>
  <text class="spec" x="8" y="834" font-size="18">80 proof</text>
  <text class="spec" x="260" y="837" text-anchor="middle" font-size="24">750 ml</text>
  <text class="spec" x="512" y="834" text-anchor="end" font-size="18">40% alc/vol</text>

  <rect class="bottom-rule" x="0" y="855" width="520" height="5" fill="var(--flag-red)"/>
  <rect class="star-band" role="img" aria-label="Navy band with a row of small stars" x="0" y="863" width="520" height="22" fill="var(--navy)"/>
  <text class="origin" x="260" y="903" text-anchor="middle" font-size="13" letter-spacing="2">HANDCRAFTED IN THE USA</text>
  <rect class="bottom-stripe" x="0" y="910" width="520" height="20" fill="var(--flag-red)"/>
</svg>
</body>
</html>
```